Rotaform Brochure

We need a conference brochure designed with a copy ready for print and also a PDF copy for email usage. We have mocked up something in word with the wording, the specific ads and images are provided in the file crate folder.

https://www.filecrate.net/sh/qk4tr82mxp51c07/HvLnQbsWERk?n=57104362

Reason: I have extended the deadline and offered more money as we understand the work is required.

```html
<!DOCTYPE html>
<html lang="en">
<head>
<meta charset="utf-8">
<title>Welcome to Rotaform 2014 – Destination Sydney</title>
<link rel="stylesheet" href="https://fonts.googleapis.com/css2?family=Carlito:wght@400;700&display=swap">
<style>
  :root {
    --navy: #1f3f86;
    --sky: #1ea6df;
    --sky-soft: rgba(30, 166, 223, 0.45);
    --ink: #3a3a3a;
    --paper: #ffffff;
    --photo-sky: #6fb0dc;
    --photo-stone: #c9c6c0;
    --photo-city: #8a96a6;
  }
  * { margin: 0; padding: 0; box-sizing: border-box; }
  html, body { width: 1200px; height: 832px; overflow: hidden; background: var(--paper); }
  body { font-family: "Carlito", Calibri, Arial, sans-serif; color: var(--ink); }
  .spread { position: relative; width: 1200px; height: 832px; overflow: hidden; }

  .page-title {
    position: absolute; left: 45px; top: 66px;
    font-size: 34px; line-height: 40px; font-weight: 700; color: var(--navy); white-space: nowrap;
  }
  .photo { position: absolute; }
  .photo-beach {
    left: 593px; top: 0; width: 607px; height: 477px;
    background: linear-gradient(180deg, var(--photo-sky) 0%, #a9cde6 30%, #dcdad5 55%, var(--photo-stone) 100%);
  }
  .photo-city {
    left: 0; top: 248px; width: 593px; height: 229px;
    background: linear-gradient(180deg, #b7a98f 0%, var(--photo-city) 55%, #5d7088 80%, #44607e 100%);
  }
  .destination-band {
    position: absolute; left: 990px; top: 142px; width: 210px; height: 98px;
    background: var(--sky-soft);
  }
  .destination-banner {
    position: absolute; left: 600px; top: 142px; width: 390px; height: 98px;
    background: var(--sky); color: #fff; white-space: nowrap;
    display: flex; align-items: center; justify-content: flex-end; padding-right: 28px;
    font-size: 37px; font-weight: 700; letter-spacing: 0.3px;
  }

  .body-text { position: absolute; font-size: 9.8px; line-height: 17.3px; }
  .body-text p { margin: 0; }
  .col-welcome-a { left: 8px; top: 488px; width: 264px; }
  .col-welcome-b { left: 282px; top: 488px; width: 275px; }
  .col-city { left: 622px; top: 486px; width: 574px; line-height: 21.4px; }

  .contact-box {
    position: absolute; left: 282px; top: 688px; width: 273px; height: 100px;
    background: var(--sky); color: #fff; font-weight: 700; font-style: normal;
    font-size: 9.8px; line-height: 12.4px; padding: 7px 16px;
  }

  .info-col { position: absolute; top: 676px; font-size: 9.8px; line-height: 16.2px; }
  .info-col h2 { font-size: 14px; font-weight: 700; color: var(--navy); line-height: 22px; margin-bottom: 2px; }
  .info-flight { left: 622px; width: 176px; }
  .info-hotel { left: 807px; width: 168px; }
  .info-insurance { left: 987px; width: 200px; }

  .folio { position: absolute; top: 815px; font-size: 9px; line-height: 12px; }
  .folio-left { left: 537px; }
  .folio-right { left: 1190px; }
</style>
</head>
<body>
<main class="spread">
  <div class="photo photo-beach" role="img" aria-label="Photograph of curved stone steps leading down to a Sydney beach under a blue sky"></div>
  <div class="photo photo-city" role="img" aria-label="Photograph of the Sydney skyline and harbour opera house at dusk"></div>

  <h1 class="page-title">WELCOME TO ROTAFORM 2014</h1>
  <div class="destination-band"></div>
  <div class="destination-banner">DESTINATION SYDNEY</div>

  <section class="body-text col-welcome-a">
    <p>The rotational moulding in dustry is on its way to Sydney, Australia and we would like you to join us.</p>
    <p>MNA believes networking isn't a buzz word, it's a necessity for your business to thrive. We are certain knowledge is essential to the health of your business and we consider that only those companies who strive to be the best truly understand the power of working together for a common goal. If you agree you need to be at Rotaform 2014 in Sydney.</p>
    <p>Since 2008 almost everything in our businesses has changed. Institutions such as banks, governments and authorities are no longer seen as reliable. Almost all company management teams have never experienced the drastic downturn in the economy and the global challenges we continue to see in this new business environment. Yet some businesses, even those in the rotational moulding industry continue to thrive. The lethargy of a difficult environment can make it difficult to see any value in leaving your business, yet without a wider</p>
  </section>

  <section class="body-text col-welcome-b">
    <p>perspective and the chance to enjoy the necessary luxury of time out of your business it can be impossible to see the way forward. We look forward to seeing you again for lots of fun, hard work and new opportunities. On behalf of the MNA Board of Directors, I look forward to welcoming you to Rotaform 2014</p>
    <p>&nbsp;Karen Whitfield, CEO</p>
    <p>For assistance with your registration and accommodation as well as anything else you may require please contact MNA on the below details</p>
  </section>

  <address class="contact-box">
    Tessa Marlowe<br>
    Moulders Network Australasia<br>
    PO Box 512, Toowong Qld 4066<br>
    Telephone: + 61(0) 7 3000 1234<br>
    Mobile: +61(0) 400 555 218<br>
    Facsimile: +61(0)7 3000 5678<br>
    Email: tmarlowe@mouldersnet.org
  </address>

  <section class="body-text col-city">
    <p>Sydney is the most populous city in Australia and is built around the attractions of a working harbor, Sydney provides the largest and most dynamic economy in the country, with a highly skilled, multi-lingual workforce and quality lifestyle. High-rise buildings of the central business district look across the water at green headlands of national parks and comfortable garden suburbs. To the west, the World Heritage Blue Mountains stand as a spectacular barrier to the inland, while the ever-changing moods of the Pacific Ocean dominate the beaches, which stretch for miles north and south from the forbidding cliffs of Sydney Heads. Sydney's cultural scene is vibrant. Coogee is a trendy beachside suburb in Sydney's Eastern Suburbs, close to the city, airport and a buzzing strip of cafés, restaurants and shops. Stunning and sophisticated but free of pretention, Coogee locals embrace a laid-back, relaxed lifestyle. The jewel of Coogee is its spectacular beach, widely renowned as one of the most beautiful on the east coast of Australia.</p>
  </section>

  <section class="info-col info-flight">
    <h2>Flight Information</h2>
    <p>MNA recommends that you book your flights early and there are some great deals around at the moment. Domestic and international flights are directly into Sydney Airport. For departures we would recommend booking your flight out of Sydney after 3.00pm on Tuesday the 24th June.</p>
  </section>

  <section class="info-col info-hotel">
    <h2>Hotel Transfers</h2>
    <p>There are several options for getting to the hotel from the airport. The easiest is in a taxi and this will cost you approximately AUD$20 – AUD$30 each way. If you need assistance please contact MNA.</p>
  </section>

  <section class="info-col info-insurance">
    <h2>Travel Insurance</h2>
    <p>MNA Strongly recommends that all attendees have travel insurance. Anything can happen while overseas from injuring yourself to covering your conference costs if you are unable to attend at the last minute. If you need assistance with this please contact MNA.</p>
  </section>

  <span class="folio folio-left">2</span>
  <span class="folio folio-right">3</span>
</main>
</body>
</html>
```